Tariq Goldsmiths Stationary Contest

Pakistan’s largest Jewellery, Diamond and luxury watches store requires professional stationery. We have a long list of are trusted clients since 1959, our third generation has successfully maintained and sustained the legacy and excellence in the sector.

We require stationery template as part of this contest. The stationery can be double sided.

We prefer a design that makes use of some of the premium business stationery printing options, such as foil stamping, embossing/debossing, painted edges, spot UV etc (doesn't have to use all these options, only what you feel works, but we are looking for a design that stands out and is memorable and these nice touches have that effect.)

We want an eye catching, innovative, high end professional looking stationery for an out of box design that blends well with our new logo (attached). We want the design to be an out of box solution, you may use any element to compliment the logo. You may consider incorporating watermark etc, highlighting our products (Gold and Diamond Jewellery in addition to Luxury watches)

Company details are as follows;

Company name: Tariq Goldsmiths
Contact Person: Farhan Qureshi
Designation: Business Development Consultant
Mobile: +92 333 815 6042
Email: farhanqureshi@mailvale.com
Website: www.tariqgoldsmiths.com

Target Market(s)

Matrimonial, Elite & Businesses class, Upmarket

Font styles to use
Other font styles liked:
• Designers choice

Colors

Designer to choose colors to be used in the design.

Requirements
Must have
• Look and feel: Upmarket, innovative, Modern, Professional, graceful, Elegant, designer stuff.
Nice to have
• Unique design

```html
<!DOCTYPE html>
<html lang="en">
<head>
<meta charset="utf-8">
<title>Tariq Goldsmiths – Business Card</title>
<link rel="stylesheet" href="https://fonts.googleapis.com/css2?family=Roboto:wght@400;500;700&display=swap">
<style>
  :root {
    --stage: #2b2521;
    --card: #1c1d1f;
    --gold: #d9a22a;
    --ink-light: #f1f1f1;
    --ink-soft: #c9c9c9;
  }
  * { margin: 0; padding: 0; box-sizing: border-box; }
  html, body {
    width: 1200px; height: 769px; overflow: hidden;
    background: var(--stage);
    font-family: "Roboto", Arial, sans-serif;
  }
  .stage {
    position: relative; width: 1200px; height: 769px;
    display: flex; align-items: center; justify-content: center; gap: 60px;
  }
  .card {
    position: relative; width: 520px; height: 297px;
    background: var(--card);
    box-shadow: 0 12px 30px rgba(0,0,0,.45);
  }
  /* front */
  .brand {
    position: absolute; left: 42px; top: 58px;
    display: flex; align-items: center; gap: 12px;
  }
  .brand-dot {
    width: 30px; height: 30px; border-radius: 50%;
    background: var(--gold);
  }
  .brand-name {
    color: var(--gold); font-weight: 700; font-size: 22px;
    letter-spacing: 1px; text-transform: uppercase;
  }
  .person {
    position: absolute; right: 46px; top: 118px; text-align: right;
  }
  .person-name {
    color: var(--gold); font-weight: 700; font-size: 19px;
    text-transform: uppercase;
  }
  .person-role {
    color: var(--ink-light); font-size: 13px; margin-top: 4px;
  }
  .accent-bar {
    position: absolute; right: 18px; top: 112px;
    width: 9px; height: 30px; background: var(--gold);
  }
  .contacts {
    position: absolute; left: 42px; bottom: 34px;
    list-style: none; display: grid; gap: 5px;
  }
  .contacts li {
    display: flex; align-items: center; gap: 10px;
    color: var(--ink-light); font-size: 14px;
  }
  .contacts svg { width: 13px; height: 13px; flex: none; }
  /* back */
  .card-back {
    display: flex; flex-direction: column; align-items: center; justify-content: center;
  }
  .card-back .brand { position: static; flex-direction: column; gap: 14px; }
  .card-back .brand-dot { width: 36px; height: 36px; }
  .card-back .brand-name { font-size: 26px; letter-spacing: 1.5px; }
  .site {
    margin-top: 22px; color: var(--ink-light);
    font-size: 13px; letter-spacing: 4px;
  }
</style>
</head>
<body>
<main class="stage">
  <section class="card card-front">
    <div class="brand">
      <span class="brand-dot"></span>
      <span class="brand-name">Tariq Goldsmiths</span>
    </div>
    <span class="accent-bar"></span>
    <div class="person">
      <p class="person-name">Farhan Qureshi</p>
      <p class="person-role">Business Development Consultant</p>
    </div>
    <ul class="contacts">
      <li>
        <svg viewBox="0 0 14 14" aria-hidden="true"><rect x="3" y="0.8" width="8" height="12.4" rx="1.4" fill="none" stroke="#d9a22a" stroke-width="1.6"/><circle cx="7" cy="10.8" r="0.9" fill="#d9a22a"/></svg>
        +92 333 815 6042
      </li>
      <li>
        <svg viewBox="0 0 14 14" aria-hidden="true"><rect x="0.5" y="2.5" width="13" height="9" fill="#d9a22a"/><path d="M0.5 2.5 L7 8 L13.5 2.5" fill="none" stroke="#1c1d1f" stroke-width="1.2"/></svg>
        farhanqureshi@mailvale.com
      </li>
      <li>
        <svg viewBox="0 0 14 14" aria-hidden="true"><circle cx="7" cy="7" r="6.3" fill="#d9a22a"/><path d="M1 7 H13 M7 0.7 C4 4 4 10 7 13.3 M7 0.7 C10 4 10 10 7 13.3" fill="none" stroke="#1c1d1f" stroke-width="1"/></svg>
        www.tariqgoldsmiths.com
      </li>
    </ul>
  </section>

  <section class="card card-back">
    <div class="brand">
      <span class="brand-dot"></span>
      <span class="brand-name">Tariq Goldsmiths</span>
    </div>
    <p class="site">www.tariqgoldsmiths.com</p>
  </section>
</main>
</body>
</html>
```